Tamsin's Crest CBD Packaging and Branding

We are looking for packaging designs for a new doctor focused CBD brand that is disease specific formulations (i.e. Bone and Joint Formula, Pelvic Formula, Pain Formula, Inflammation Formula, ect.) We would like the first packaging prototype to be our Pain Formulation. Our tagline is, "The Tamsin's Crest" & we would also like the phrase, "Life. Balanced." - We are looking for our Logo to be on the box as well. We currently need a logo as well. We would like the letters "KT" to be more prominent than "nuvo" Our first product will be SoftGels and the active ingredient list can be made up at the moment. Our brand and packaging needs to convey authority, trust and scientific knowledge (since all of our formulations are created by researched and renowned doctors and scientists), but we also don't want to be too clinical feeling, so adding a modern touch. Attached are some sample designs for reference (none are the final iteration) as well as some vectorized art.

Target Market(s)

40-60 year old patients

Industry/Entity Type

Medical And Science

Logo Text

KT Nuvo

Requirements
Must have
• Clean, professional and trusting medical designs with a modern touch. New logo incorporated into the design.
Should not have
• Not too clinical feeling - Not pharmaceutical

```html
<!DOCTYPE html>
<html lang="en">
<head>
<meta charset="utf-8">
<title>Tamsin's Crest – Comfort Pain Relief Carton</title>
<link rel="stylesheet" href="https://fonts.googleapis.com/css2?family=Oswald:wght@500;600&family=Poppins:wght@400;500;600;700&family=Russo+One&family=Zilla+Slab:wght@700&display=swap">
<style>
  :root {
    --paper: #ffffff;
    --panel-light: #f7f8f9;
    --panel-mid: #e6e8eb;
    --blue-deep: #1d56a8;
    --blue-bright: #2a9be0;
    --teal: #0d85ae;
    --ink: #2c3038;
    --ink-soft: #4a4f58;
    --logo-blue: #1f6fc0;
    --cut: #e0323a;
    --white: #ffffff;
  }
  * { box-sizing: border-box; margin: 0; padding: 0; }
  html, body { width: 800px; height: 1200px; overflow: hidden; background: var(--paper); }
  .canvas { position: relative; width: 800px; height: 1200px; background: var(--paper); }
  .dieline { position: absolute; inset: 0; }
  .carton { position: absolute; left: 79px; top: 452px; width: 682px; height: 357px; display: flex; }
  .panel { position: relative; height: 100%; overflow: hidden;
    background: linear-gradient(180deg, var(--panel-mid) 0%, var(--panel-light) 45%, var(--white) 75%); }
  .panel--front { width: 213px; }
  .panel--side { width: 128px; }
  .panel--front:first-child { width: 212px; }
  .panel--side:nth-child(2) { width: 129px; }
  .band-top { position: absolute; left: 0; right: 0; top: 0; height: 17px;
    background: linear-gradient(90deg, var(--blue-deep), var(--blue-bright) 70%, var(--blue-deep)); }
  .band-bottom { position: absolute; left: 0; right: 0; bottom: 0; height: 78px;
    background: linear-gradient(90deg, var(--blue-bright) 0%, #2486d2 50%, var(--blue-deep) 100%); }
  .figure { position: absolute; z-index: 1; border-radius: 40px 40px 10px 10px;
    background: linear-gradient(180deg, #ee8b5c 0%, #4fa3a6 35%, #7b4fb5 65%, #d0487d 100%); opacity: .85; }
  .figure--edge { left: 0; top: 22px; width: 34px; height: 257px; border-radius: 0 30px 10px 0; }
  .figure--spread { left: 371px; top: 22px; width: 102px; height: 257px; }
  .brandmark { position: absolute; text-align: center; z-index: 2; }
  .brandmark__name { display: flex; align-items: center; justify-content: center; gap: 4px;
    font-family: "Poppins", sans-serif; font-weight: 600; font-size: 22px; color: var(--logo-blue); line-height: 1; }
  .brandmark__dot { width: 8px; height: 8px; border-radius: 50%; background: var(--logo-blue); }
  .brandmark__tagline { margin-top: 5px; font-family: "Poppins", sans-serif; font-size: 6.5px;
    letter-spacing: 1.8px; color: var(--ink-soft); text-transform: uppercase; }
  .front-copy { position: absolute; left: 0; right: 0; top: 0; bottom: 0; z-index: 2; }
  .front-copy .brandmark { left: 40px; right: 0; top: 30px; }
  .claim { position: absolute; left: 60px; right: 0; top: 118px; text-align: center;
    font-family: "Oswald", sans-serif; font-weight: 500; font-size: 17px; line-height: 23px; color: var(--ink-soft); }
  .product { position: absolute; left: 30px; right: 0; top: 185px; text-align: center; }
  .product__name { font-family: "Russo One", sans-serif; font-size: 33px; color: var(--teal); line-height: 1; }
  .product__use { margin-top: 6px; font-family: "Poppins", sans-serif; font-weight: 600; font-size: 11.5px; color: var(--ink); letter-spacing: .3px; }
  .dose { position: absolute; left: 0; right: 0; bottom: 0; height: 78px; z-index: 2;
    text-align: center; color: var(--white); padding-top: 8px; }
  .dose__form { font-family: "Poppins", sans-serif; font-weight: 600; font-size: 10px; letter-spacing: .4px; }
  .dose__strength { font-family: "Poppins", sans-serif; font-weight: 600; font-size: 21px; line-height: 26px; }
  .dose__count { font-family: "Zilla Slab", serif; font-weight: 700; font-size: 13px; }
  .panel--front:first-child .dose { padding-left: 12px; }
  .side-copy { position: absolute; left: 12px; right: 6px; z-index: 2; color: var(--ink); }
  .side-title { font-family: "Oswald", sans-serif; font-weight: 600; font-size: 19px; line-height: 26px; color: var(--ink-soft); }
  .side-heading { font-family: "Oswald", sans-serif; font-weight: 500; font-size: 11px; color: var(--ink); }
  .side-body { font-family: "Oswald", sans-serif; font-weight: 500; font-size: 7px; line-height: 10.5px; color: var(--ink-soft); }
  .side-title--centred { text-align: center; }
  .nutrition { position: absolute; left: 6px; width: 114px; top: 141px; height: 120px; z-index: 2;
    border: 0.8px solid var(--ink-soft); background: var(--white); padding: 5px 4px; }
  .nutrition__title { font-family: "Oswald", sans-serif; font-weight: 600; font-size: 12px; color: var(--ink); padding-bottom: 3px; border-bottom: 2px solid var(--ink); }
  .nutrition__row { font-family: "Oswald", sans-serif; font-weight: 500; font-size: 6.2px; line-height: 9px; color: var(--ink-soft); padding: 4px 2px; }
  .nutrition__row + .nutrition__row { border-top: 1px solid var(--ink); }
  .nutrition__row--rule { border-top-width: 2px !important; }
  .nutrition__row--right { text-align: right; }
  .ingredients { position: absolute; left: 8px; right: 6px; bottom: 0; height: 78px; z-index: 2; color: var(--white); padding-top: 12px; }
  .ingredients__title { font-family: "Oswald", sans-serif; font-weight: 500; font-size: 10px; }
  .ingredients__body { margin-top: 3px; font-family: "Oswald", sans-serif; font-size: 7px; line-height: 10.5px; }
</style>
</head>
<body>
<div class="canvas">
  <svg class="dieline" width="800" height="1200" viewBox="0 0 800 1200" fill="none" stroke="var(--cut)" stroke-width="0.8">
    <!-- top tuck flap -->
    <path d="M79,452 L79,326 L82,326 L82,324 L79,324 L80,316 Q86,290 112,290 L258,290 Q282,290 290,316 L291,324 L288,324 L288,326 L291,326 L291,452"/>
    <line x1="94" y1="327" x2="276" y2="327"/>
    <!-- top dust flaps -->
    <path d="M291,452 L301,441 L302,377 L398,377 L415,441 L420,452"/>
    <path d="M633,452 L642,440 L657,377 L750,377 L752,440 L761,452"/>
    <!-- glue flap -->
    <path d="M79,464 L40,476 L40,770 L79,809"/>
    <!-- bottom lock flaps -->
    <path d="M79,809 L88,908 L283,908 L283,852 L264,841 L184,888 L214,866 L279,829 L291,809"/>
    <path d="M291,809 L301,900 L358,900 L420,836 L420,809"/>
    <path d="M420,809 L429,908 L624,908 L624,852 L605,841 L525,888 L555,866 L620,829 L633,809"/>
    <path d="M633,809 L646,900 L698,900 L761,836 L761,809"/>
  </svg>

  <div class="carton">
    <section class="panel panel--front">
      <div class="band-top"></div>
      <div class="band-bottom"></div>
      <div class="figure figure--edge" role="img" aria-label="Colourful anatomical muscle figure illustration"></div>
      <div class="front-copy">
        <div class="brandmark">
          <div class="brandmark__name"><span>KT Nuvo</span><span class="brandmark__dot"></span></div>
          <div class="brandmark__tagline">The Tamsin's Crest</div>
        </div>
        <p class="claim">Life<br>Balanced</p>
        <div class="product">
          <div class="product__name">COMFORT</div>
          <div class="product__use">PAIN RELIEF</div>
        </div>
      </div>
      <div class="dose">
        <div class="dose__form">SOFT GELS</div>
        <div class="dose__strength">50 mg CBD</div>
        <div class="dose__count">30 COUNT</div>
      </div>
    </section>

    <section class="panel panel--side">
      <div class="band-bottom" style="background: var(--blue-deep);"></div>
      <div class="side-copy" style="top: 40px;">
        <p class="side-title">The<br>Tamsin's<br>Crest</p>
      </div>
      <div class="side-copy" style="top: 165px;">
        <p class="side-heading">Sugested use :</p>
        <p class="side-body">Consult your pharmacist<br>or Physician before use .</p>
        <p class="side-heading" style="margin-top: 12px;">Distributed by :</p>
        <p class="side-body">Harlow Ridge Labs<br>4120 Quarry Lane, Millbrook ,<br>United States</p>
      </div>
    </section>

    <section class="panel panel--front">
      <div class="band-top"></div>
      <div class="band-bottom"></div>
      <div class="front-copy">
        <div class="brandmark">
          <div class="brandmark__name"><span>KT Nuvo</span><span class="brandmark__dot"></span></div>
          <div class="brandmark__tagline">The Tamsin's Crest</div>
        </div>
        <p class="claim">Life<br>Balanced</p>
        <div class="product">
          <div class="product__name">COMFORT</div>
          <div class="product__use">PAIN RELIEF</div>
        </div>
      </div>
      <div class="dose">
        <div class="dose__form">SOFT GELS</div>
        <div class="dose__strength">50 mg CBD</div>
        <div class="dose__count">30 COUNT</div>
      </div>
    </section>

    <section class="panel panel--side">
      <div class="band-bottom" style="background: linear-gradient(90deg, #2486d2, var(--blue-deep));"></div>
      <div class="side-copy" style="top: 40px; left: 4px;">
        <p class="side-title side-title--centred">The Tamsin's<br>Crest</p>
      </div>
      <div class="nutrition">
        <p class="nutrition__title">Nutrition Facts:</p>
        <p class="nutrition__row">serving size : 1 softgel<br>serving per container : 30</p>
        <p class="nutrition__row nutrition__row--rule nutrition__row--right">Amount per serving : %DV</p>
        <p class="nutrition__row">Cannabidal(CBD): 25mg</p>
        <p class="nutrition__row nutrition__row--rule">percent daily Values(DV)<br>not established</p>
      </div>
      <div class="ingredients">
        <p class="ingredients__title">Other Ingradients:</p>
        <p class="ingredients__body">Grape seed oil, Vegetariansoftgel vegetable Cellulore , water ,Silica loren ipsum, lorenipsum ,lorenips</p>
      </div>
    </section>

    <div class="figure figure--spread" role="img" aria-label="Colourful anatomical muscle figure illustration"></div>
  </div>
</div>
</body>
</html>
```